Darrow Consulting needs a quality & professional business card!

I am a recruitment and employment consultant from Brisbane, Australia and I had a fantastic logo organised by this community to I am hoping the business card will be the same.

I have attached the Darrow consulting logo that ideally would feature on the back of the business card. There are a number of logos for you to use as you see fit. I would like the colour cheme to match that of the Darrow Consulting logo. I also have a secondary company called Career Lantern Australia and I have included that logo as well. While it is an important part of the business I don't want this logo feature too predominantly as I am moving out of this space. This logo was created by myself and is of low quality. Feel free to use the icon and words however you want. The winning design will be smart, professional and eye-catching.

The information I am looking for in the business card is:
Name: Gavin Darrow
Position: Founder & Director
Phone: (07) 3519 6482
Mobile: 0431 586 207
Email: gavin@careerlantern.com.au

Target Market(s)

Recruiters, government, large companies

Contact Information for Business Card

Name: Gavin Darrow
Phone: (07) 3519 6482
Mobile: 0431 586 207
Web: www.careerlantern.com.au

Font styles to use
Serif
Sans Serif

Requirements
Must have
• Darrow Consulting Logo on reverse side
• Contact details on front side with smaller reference to Darrow Consulting logo and Career Lantern Australia logo

```html
<!DOCTYPE html>
<html lang="en">
<head>
<meta charset="utf-8">
<title>Darrow Consulting – Business Card</title>
<link href="https://fonts.googleapis.com/css2?family=Montserrat:wght@400;600;700&display=swap" rel="stylesheet">
<style>
  :root {
    --bg: #c3e6db;
    --charcoal: #272a2e;
    --silver: #cdcecf;
    --silver-dark: #a9abad;
    --white: #ffffff;
    --ink: #2a2d31;
    --orange: #e8892b;
    --green: #2fae4e;
    --blue: #2b8fd8;
    --text-light: #eef0f1;
  }
  * { box-sizing: border-box; margin: 0; padding: 0; }
  html, body { width: 1200px; height: 856px; overflow: hidden; }
  body {
    background: var(--bg);
    font-family: "Montserrat", sans-serif;
    position: relative;
  }
  .card {
    position: absolute;
    top: 263px;
    width: 540px;
    height: 330px;
    border-radius: 24px;
    overflow: hidden;
    box-shadow: 0 10px 28px rgba(40, 80, 70, 0.18);
  }

  /* ---------- Front ---------- */
  .card-front { left: 40px; background: var(--white); }
  .front-brands {
    position: absolute; left: 30px; top: 140px;
    display: flex; flex-direction: column; gap: 22px;
  }
  .brand-primary {
    display: flex; align-items: center; gap: 10px;
    font-weight: 600; font-size: 19px; color: var(--ink); letter-spacing: 0.5px;
  }
  .brand-mark { width: 16px; height: 16px; background: var(--ink); }
  .brand-secondary {
    font-weight: 600; font-size: 13px; color: var(--ink); letter-spacing: 0.3px;
  }
  .dark-panel {
    position: absolute; left: 250px; top: 0; right: 0; bottom: 0;
    background: var(--charcoal);
  }
  .top-strip {
    position: absolute; left: 250px; top: 0; right: 0; height: 22px;
    background: var(--silver);
  }
  .accent { position: absolute; left: 250px; width: 7px; }
  .accent-orange { top: 22px; height: 24px; background: var(--orange); }
  .accent-green { top: 118px; height: 60px; background: var(--green); }
  .accent-blue { top: 262px; height: 68px; background: var(--blue); }
  .name-ribbon {
    position: absolute; left: 232px; top: 44px; width: 236px; height: 56px;
    background: var(--silver);
    padding: 9px 0 0 30px;
    color: var(--ink);
  }
  .person-name { font-weight: 700; font-size: 19px; line-height: 1.1; }
  .person-title { font-weight: 400; font-size: 12px; margin-top: 2px; }
  .contact-list { position: absolute; left: 0; top: 0; list-style: none; }
  .contact-row { position: absolute; display: flex; align-items: center; gap: 14px; }
  .contact-tag { width: 44px; height: 26px; display: block; }
  .contact-text { color: var(--text-light); font-size: 14px; letter-spacing: 0.3px; white-space: nowrap; }

  /* ---------- Back ---------- */
  .card-back { left: 620px; background: var(--charcoal); }
  .corner { position: absolute; background: var(--silver); }
  .corner-tl { left: 0; top: 0; width: 120px; height: 140px; clip-path: polygon(0 0, 100% 0, 0 100%); }
  .corner-br { right: 0; bottom: 0; width: 120px; height: 140px; clip-path: polygon(100% 0, 100% 100%, 0 100%); }
  .back-brand {
    position: absolute; left: 0; right: 0; top: 0; bottom: 0;
    display: flex; align-items: center; justify-content: center;
    font-weight: 600; font-size: 26px; letter-spacing: 3px;
    color: var(--silver); text-transform: uppercase;
  }
</style>
</head>
<body>

  <section class="card card-front" aria-label="Business card front">
    <div class="dark-panel"></div>
    <div class="top-strip"></div>
    <div class="accent accent-orange"></div>
    <div class="accent accent-green"></div>
    <div class="accent accent-blue"></div>

    <div class="front-brands">
      <div class="brand-primary"><span class="brand-mark"></span>Darrow Consulting</div>
      <div class="brand-secondary">Career Lantern Australia</div>
    </div>

    <div class="name-ribbon">
      <p class="person-name">Gavin Darrow</p>
      <p class="person-title">Founder &amp; Director</p>
    </div>

    <ul class="contact-list">
      <li class="contact-row" style="left:248px; top:134px;">
        <svg class="contact-tag" viewBox="0 0 44 26" aria-hidden="true">
          <polygon points="0,0 34,0 44,13 34,26 0,26" fill="#cdcecf"/>
          <circle cx="22" cy="13" r="8" fill="none" stroke="#2a2d31" stroke-width="1.4"/>
          <path d="M18.5 9.5c0 4 2.5 7 6.5 7l1-1.6-2-1-1 .8c-1.2-.6-2-1.4-2.5-2.5l.8-1-1-2z" fill="#2a2d31"/>
        </svg>
        <span class="contact-text">(07) 3519 6482</span>
      </li>
      <li class="contact-row" style="left:258px; top:176px;">
        <svg class="contact-tag" viewBox="0 0 44 26" aria-hidden="true">
          <polygon points="0,0 34,0 44,13 34,26 0,26" fill="#cdcecf"/>
          <circle cx="22" cy="13" r="8" fill="none" stroke="#2a2d31" stroke-width="1.4"/>
          <rect x="19.5" y="8.5" width="5" height="9" rx="1" fill="none" stroke="#2a2d31" stroke-width="1.2"/>
        </svg>
        <span class="contact-text">0431 586 207</span>
      </li>
      <li class="contact-row" style="left:268px; top:218px;">
        <svg class="contact-tag" viewBox="0 0 44 26" aria-hidden="true">
          <polygon points="0,0 34,0 44,13 34,26 0,26" fill="#cdcecf"/>
          <circle cx="22" cy="13" r="8" fill="#2a2d31"/>
          <rect x="18" y="10" width="8" height="6" fill="#cdcecf"/>
          <path d="M18 10l4 3.5 4-3.5" fill="none" stroke="#2a2d31" stroke-width="1"/>
        </svg>
        <span class="contact-text">gavin@careerlantern.com.au</span>
      </li>
      <li class="contact-row" style="left:278px; top:260px;">
        <svg class="contact-tag" viewBox="0 0 44 26" aria-hidden="true">
          <polygon points="0,0 34,0 44,13 34,26 0,26" fill="#cdcecf"/>
          <circle cx="22" cy="13" r="8" fill="#2a2d31"/>
          <circle cx="22" cy="13" r="5" fill="none" stroke="#cdcecf" stroke-width="1"/>
          <path d="M17 13h10M22 8c-2 3-2 7 0 10M22 8c2 3 2 7 0 10" fill="none" stroke="#cdcecf" stroke-width="0.9"/>
        </svg>
        <span class="contact-text">www.careerlantern.com.au</span>
      </li>
    </ul>
  </section>

  <section class="card card-back" aria-label="Business card back">
    <div class="corner corner-tl"></div>
    <div class="corner corner-br"></div>
    <div class="back-brand">Darrow Consulting</div>
  </section>

</body>
</html>
```